Broschüren-Design für Produzent von hochwertigen Verpackungs- und Präsentationslösungen
Zielgruppe
Wir produzieren hochwertige Verpackungs- und Präsentationslösungen.
Unsere Zielgruppe sind Firmen, welche kreative Premium-Packaging benötigt.
Aufgabenstellung
- Format: A4 hoch
- Umfang: 6 Seiten
- Falzart: Wickelfalz
- Design muss sehr hochwertig sein. Passend zu unseren Produktion (siehe Bilder)
- Wir möchten mit diesem Falzprospekt eine Übersicht über unsere Produkte generieren.
- Die Produkte sind bereits schon hochwertig fotografiert und müssen in einem anspruchsvollen Design in Szene gesetzt werden.
- Der Prospekt sollte die Kunden emotional berühren.
- Auf der Titelseite werden wir den Titel «High Performance Packaging» mit Folien prägen
- Seitenaufbau gemäss meiner Visualisierung (im Anhang)
- Bei jeder Produktkategorie möchte ich ein Grosses Übersichtsbild zusammen mit einem kurzen Text.
Ergänzend können noch weitere (passende) Bilder der jeweiligen Kategorie abgebildet werden.
Im Anhang finden Sie:
- Visualisierung des zu gestaltenden Prospekt
- Werbeflyer (zur Ansicht/Inspiration). In etwa so stellen wir uns das Design/Tonalität vor.
- Weitere passende Produktbilder können vorerst auf der Webseite unseres Produktionspartner (www.bogenhaus.de) entnommen werden.

```html
<!DOCTYPE html>
<html lang="de">
<head>
<meta charset="utf-8">
<title>Falzprospekt – Innenseiten</title>
<link href="https://fonts.googleapis.com/css2?family=Barlow:wght@600&family=Poppins:wght@300;400;600&display=swap" rel="stylesheet">
<style>
  :root{
    --canvas:#e8e8e8;
    --page-light:#e4e4e4;
    --page-grey:#c2c2c2;
    --panel:#3a3e4b;
    --panel-line:#8a8e9a;
    --panel-text:#d6d8de;
    --ink:#2a2a2a;
    --ink-soft:#555;
    --rule:#7a7a7a;
    --folio:#d0d0d0;
  }
  *{box-sizing:border-box;margin:0;padding:0}
  html,body{width:1200px;height:804px;overflow:hidden;background:var(--canvas)}
  body{font-family:"Poppins",sans-serif;position:relative}
  .spread{position:absolute;left:63px;top:22px;width:1074px;height:760px;display:flex;box-shadow:0 4px 18px rgba(0,0,0,.12)}
  .page{position:relative;width:537px;height:760px;overflow:hidden}
  .page--products{background:var(--page-light)}
  .page--intro{background:var(--page-grey)}

  .photo{position:absolute}
  .photo--boxes{left:26px;top:92px;width:282px;height:196px;background:linear-gradient(160deg,#2a2b2f,#5a5b60 55%,#1f2023)}
  .photo--folders{left:26px;top:288px;width:282px;height:196px;background:linear-gradient(150deg,#2c2c30,#8a2a30 55%,#2a2a2d)}
  .photo--samples{left:26px;top:484px;width:282px;height:198px;background:linear-gradient(170deg,#3a3a3d,#6c6560 60%,#2b2b2e)}
  .photo--strip{left:480px;top:92px;width:57px;height:590px;background:linear-gradient(180deg,#4a4c50,#9ea2aa 45%,#2e2f33)}

  .category-panel{position:absolute;left:308px;top:92px;width:172px;height:590px;background:var(--panel);padding:26px 16px 0 18px;color:var(--panel-text)}
  .category{padding-bottom:22px;margin-bottom:24px;border-bottom:1px dotted var(--panel-line)}
  .category:last-child{border:none}
  .category__title{font-weight:600;font-size:9.5px;letter-spacing:.06em;color:#fff;margin-bottom:6px}
  .category__text{font-weight:300;font-size:7.6px;line-height:1.55}

  .folio{position:absolute;right:20px;bottom:18px;font-family:"Barlow",sans-serif;font-weight:600;font-size:16px;color:var(--folio)}
  .page--intro .folio{color:#d6d6d6}

  .rule{position:absolute;left:58px;right:58px;border-top:1px dotted var(--rule)}
  .rule--top{top:78px}
  .rule--bottom{top:660px}

  .intro{position:absolute;left:100px;top:150px;width:360px}
  .intro__headline{font-family:"Barlow",sans-serif;font-weight:600;font-size:27px;line-height:1.05;letter-spacing:.02em;color:var(--ink);margin-bottom:22px}
  .intro__text{font-weight:300;font-size:7.6px;line-height:1.55;color:var(--ink-soft);margin-bottom:10px;padding-left:16px}

  .benefits{position:absolute;left:100px;top:410px;width:320px;list-style:none}
  .benefit{display:flex;align-items:center;gap:22px;padding:12px 0;border-bottom:1px dotted var(--rule)}
  .benefit:last-child{border:none}
  .benefit svg{width:24px;height:24px;flex:none;stroke:var(--ink);fill:none;stroke-width:1.2;stroke-linecap:round;stroke-linejoin:round}
  .benefit__title{font-weight:600;font-size:8px;color:var(--ink)}
  .benefit__text{font-weight:300;font-size:7.6px;line-height:1.45;color:var(--ink-soft)}
</style>
</head>
<body>
<main class="spread">
  <section class="page page--products">
    <div class="photo photo--boxes" role="img" aria-label="Produktfoto: Geschenkboxen mit Einlage, Stift und Taschenmesser auf dunklem Grund"></div>
    <div class="photo photo--folders" role="img" aria-label="Produktfoto: Präsentationsmappen in Rot und Dunkelblau"></div>
    <div class="photo photo--samples" role="img" aria-label="Produktfoto: Mustermappen mit Farbmustern"></div>
    <div class="photo photo--strip" role="img" aria-label="Produktfoto: helle Verpackungen, Ausschnitt"></div>
    <div class="category-panel">
      <article class="category">
        <h2 class="category__title">VERPACKUNGEN</h2>
        <p class="category__text">Präsentationsmappen Lorem ipsum dolor sit amet, consetetur sadipscing elitr, sed diam nonumy eirmod tempor invidunt ut labore et dolore magna aliquyam erat, sed diam voluptua. At vero eos et accusam et justo duo dolores et ea rebum. Stet clita kasd.</p>
      </article>
      <article class="category">
        <h2 class="category__title">PRÄSENTATIONSMAPPEN</h2>
        <p class="category__text">Präsentationsmappen Lorem ipsum dolor sit amet, consetetur sadipscing elitr, sed diam nonumy eirmod tempor invidunt ut labore et dolore magna aliquyam erat, sed diam voluptua. At vero eos et accusam et justo duo dolores et ea rebum. Stet clita kasd.</p>
      </article>
      <article class="category">
        <h2 class="category__title">MUSTERMAPPEN</h2>
        <p class="category__text">Präsentationsmappen Lorem ipsum dolor sit amet, consetetur sadipscing elitr, sed diam nonumy eirmod tempor invidunt ut labore et dolore magna aliquyam erat, sed diam voluptua. At vero eos et accusam et justo duo dolores et ea rebum. Stet clita kasd.</p>
      </article>
    </div>
    <span class="folio">D</span>
  </section>

  <section class="page page--intro">
    <div class="rule rule--top"></div>
    <div class="intro">
      <h1 class="intro__headline">Höchste Qualität zu<br>unschlagbaren Preisen.</h1>
      <p class="intro__text">Mit einer unvergleichlich großen Bandbreite im Bereich des Premium Packaging bieten wir vielseitige Verpackungs und Präsentationslösungen.</p>
      <p class="intro__text">Einzigartiges Design, variable Formen und hochwertige Haptik unterstreichen die Bedeutung von Ihren Produkten.</p>
      <p class="intro__text">Überzeugen Sie sich jetzt und bestellen Sie Ihr individuelles Angebot.</p>
    </div>
    <ul class="benefits">
      <li class="benefit">
        <svg viewBox="0 0 24 24" aria-hidden="true"><path d="M8 3 3 12h3l-3 5h10l-3-5h3z"/><path d="M8 17v4"/><path d="M16 6l-3 6h2l-2 4h7l-2-4h2z"/><path d="M16 16v5M3 21h18"/></svg>
        <div><p class="benefit__title">Nachhaltige Papiere</p><p class="benefit__text">Unsere Rohmaterialien stammen aus<br>nachhaltiger Forstwirtschaft.</p></div>
      </li>
      <li class="benefit">
        <svg viewBox="0 0 24 24" aria-hidden="true"><path d="M6 9c0 6 3 11 8 11s6-4 6-8"/><path d="M10 14c2-4 6-7 10-9-1 5-4 9-9 10"/><path d="M4 6l3 3"/></svg>
        <div><p class="benefit__title">Wiederverwendbarkeit</p><p class="benefit__text">Unsere Boxen sind so schön und stabil, dass<br>man sie auf jeden Fall wiederverwendet.</p></div>
      </li>
      <li class="benefit">
        <svg viewBox="0 0 24 24" aria-hidden="true"><path d="M9 5l3-2 3 5"/><path d="M13 8h2.5"/><path d="M19 11l2 4-3 4h-4"/><path d="M14 17l-1.5 2 1.5 2"/><path d="M7 19H4l-1-3 3-5"/><path d="M4 11l2 0 1 2"/></svg>
        <div><p class="benefit__title">Recyclebare Lösungen</p><p class="benefit__text">Auf Nachfrage können wir Ihnen eine 100%<br>recyclebare Verpackung anbieten.</p></div>
      </li>
    </ul>
    <div class="rule rule--bottom"></div>
    <span class="folio">A</span>
  </section>
</main>
</body>
</html>
```